RW Frameworks Inc Business cards

We need business cards using our existing logo but slightly modified. Right now the logo says RW Framework Masonry. We want to keep the RW part of the design, but replace the Framework Masonry portion with "FRAMEWORKS". Please see the attached file.
Ideally this would be a blank template so we can add Different Names, titles, and phone numbers later.
On the one side we want only the logo and on the other side the detail. I'm attaching an example for you to see.
Please reach out with any other questions. Our address and other details will be given out once we find a design we like.

Target Market(s)

Construction Industry

```html
<!DOCTYPE html>
<html lang="en">
<head>
<meta charset="utf-8">
<title>RW Frameworks Inc – Business Cards</title>
<link rel="stylesheet" href="https://fonts.googleapis.com/css2?family=Open+Sans:wght@400;600;700&display=swap">
<style>
  :root {
    --brand-blue: #1c76bb;
    --card-white: #f1f1f3;
    --logo-grey: #808184;
    --backdrop: #cfc4ae;
  }
  * { box-sizing: border-box; margin: 0; padding: 0; }
  html, body {
    width: 1200px; height: 1200px; overflow: hidden;
    background: var(--backdrop);
    font-family: "Open Sans", Arial, sans-serif;
  }
  .canvas { position: relative; width: 1200px; height: 1200px; }

  .card {
    position: absolute;
    width: 781px; height: 469px;
    background: var(--card-white);
    overflow: hidden;
  }
  .card--details { left: 93px; top: 69px; }
  .card--logo { left: 325px; top: 650px; }

  .card__shape { position: absolute; left: 0; top: 0; }

  .contact-name {
    position: absolute; left: 124px; top: 84px;
    color: var(--card-white);
    font-size: 30px; font-weight: 400; letter-spacing: -1.2px;
    line-height: 1;
  }
  .contact-title {
    position: absolute; left: 124px; top: 128px;
    color: var(--card-white);
    font-size: 16px; letter-spacing: 0.3px; line-height: 1;
  }
  .title-rule {
    position: absolute; left: 124px; top: 164px;
    width: 31px; height: 2.5px; background: var(--card-white);
  }
  .contact-line {
    position: absolute; color: var(--card-white);
    font-size: 15.5px; line-height: 21px; left: 181px;
  }
  .contact-line--phone { top: 203px; font-size: 13.5px; }
  .contact-line--web { top: 272px; }
  .contact-line--place { top: 350px; }

  .brand {
    position: absolute;
    display: flex; flex-direction: column; align-items: center;
  }
  .brand__mark {
    color: var(--brand-blue); font-weight: 700; line-height: 1;
    letter-spacing: 4px;
  }
  .brand__tagline {
    color: var(--logo-grey); font-weight: 400; line-height: 1;
  }
  .card--details .brand { left: 481px; top: 172px; width: 208px; }
  .card--details .brand__mark { font-size: 106px; }
  .card--details .brand__tagline { font-size: 15px; letter-spacing: 11.2px; margin-top: 4px; margin-right: -11.2px; }

  .card--logo .brand { left: 252px; top: 154px; width: 276px; }
  .card--logo .brand__mark { font-size: 140px; }
  .card--logo .brand__tagline { font-size: 19px; letter-spacing: 14.6px; margin-top: 6px; margin-right: -14.6px; }
</style>
</head>
<body>
<main class="canvas">

  <section class="card card--details" aria-label="Business card, details side">
    <svg class="card__shape" width="781" height="469" viewBox="0 0 781 469" aria-hidden="true">
      <rect x="0" y="0" width="417" height="469" fill="var(--brand-blue)"/>
      <polygon points="0,0 60,63 60,413 0,469" fill="var(--card-white)"/>
      <g stroke="var(--card-white)" stroke-width="2.5">
        <line x1="60" y1="224" x2="125" y2="224"/>
        <line x1="60" y1="291" x2="125" y2="291"/>
        <line x1="60" y1="358" x2="125" y2="358"/>
      </g>
      <g fill="var(--card-white)">
        <circle cx="143" cy="224" r="20"/>
        <circle cx="143" cy="291" r="20"/>
        <circle cx="143" cy="358" r="20"/>
      </g>
      <!-- phone -->
      <path d="M134 214 c2-2 4-2 5 0 l3 4 c1 2 0 3-1 4 l-1 1 c1 3 4 6 7 7 l1-1 c1-1 2-2 4-1 l4 3 c2 1 2 3 0 5 l-2 2 c-3 2-9 0-15-6 s-8-12-6-15 z" fill="var(--brand-blue)"/>
      <!-- globe -->
      <g fill="none" stroke="var(--brand-blue)" stroke-width="1.8">
        <circle cx="142" cy="290" r="11"/>
        <ellipse cx="142" cy="290" rx="5" ry="11"/>
        <line x1="131" y1="290" x2="153" y2="290"/>
        <path d="M133 284 h18 M133 296 h18"/>
      </g>
      <path d="M146 296 l8 3 -3 1 3 3 -1 1 -3-3 -1 3 z" fill="var(--brand-blue)"/>
      <!-- pin -->
      <path d="M143 345 c-6 0-10 4-10 10 c0 6 10 16 10 16 s10-10 10-16 c0-6-4-10-10-10 z" fill="var(--brand-blue)"/>
      <circle cx="143" cy="354" r="3.5" fill="var(--card-white)"/>
    </svg>

    <h1 class="contact-name">YOUR NAME</h1>
    <p class="contact-title">DESIGNATION</p>
    <div class="title-rule"></div>

    <p class="contact-line contact-line--phone">xxx-xxx-xxxx<br>xxx-xxx-xxxx</p>
    <p class="contact-line contact-line--web">company name@email.com<br>company websitename.com</p>
    <p class="contact-line contact-line--place">company location</p>

    <div class="brand">
      <span class="brand__mark">RW</span>
      <span class="brand__tagline">FRAMEWORKS</span>
    </div>
  </section>

  <section class="card card--logo" aria-label="Business card, logo side">
    <svg class="card__shape" width="781" height="469" viewBox="0 0 781 469" aria-hidden="true">
      <polygon points="0,0 57,56 57,405 0,469" fill="var(--brand-blue)"/>
    </svg>
    <div class="brand">
      <span class="brand__mark">RW</span>
      <span class="brand__tagline">FRAMEWORKS</span>
    </div>
  </section>

</main>
</body>
</html>
```